Pizza Box 10" x 10" - color: White

Custom design, utilizing CrustVarto Logo and include the following information on the Pizza Box:

1. Custom Crafted Pizza with Quality Ingredients.
2. [....Get Your GAME ON] to be placed on the front flap and seen when the
box is opened.
3. You"ll miss 100% of the Pizza you don't eat.

4. Visit www.plenovacartons.example for additional design resource information. Go to site and then click on ORDERING to access.

5. The 10" x 10" Pizza Box is to be in the color WHITE.
6. Use colors Black and Red. no generic images. no food pics. I am looking for a clean and cool design.

Target Market(s)

Age 16 - 36 years

Industry/Entity Type

American Restaurant

Font styles to use
Sans Serif

Colors
ec1f27
000000
ffffff

Requirements
Must have
• Color Red and Black.
• Logo on Top and all sides of the Pizza Box.
Nice to have
• A Creative design that does not look generic.
Should not have
• No food images.

```html
<!DOCTYPE html>
<html lang="en">
<head>
<meta charset="utf-8">
<title>CrustVarto – You'll Miss 100% of the Pizza You Don't Eat</title>
<link rel="stylesheet" href="https://fonts.googleapis.com/css2?family=Anton&family=Archivo+Black&display=swap">
<style>
  :root {
    --red: #ec1f27;
    --black: #000000;
    --white: #ffffff;
    --slice-light: #f4f4f4;
    --slice-mid: #e2e2e2;
  }
  html, body {
    margin: 0;
    padding: 0;
    width: 1200px;
    height: 1200px;
    overflow: hidden;
    background: var(--white);
  }
  .box-top {
    display: block;
    width: 1200px;
    height: 1200px;
  }
  .brand-name {
    font-family: "Archivo Black", sans-serif;
    font-size: 38px;
    fill: var(--black);
  }
  .brand-dot { fill: var(--red); }
  .slogan-wide {
    font-family: "Archivo Black", sans-serif;
  }
  .slogan-tall {
    font-family: "Anton", sans-serif;
  }
  .ink-black { fill: var(--black); }
  .ink-red { fill: var(--red); }
</style>
</head>
<body>
<svg class="box-top" viewBox="0 0 1200 1200" xmlns="http://www.w3.org/2000/svg">
  <defs>
    <linearGradient id="sliceTone" x1="0" y1="0" x2="1" y2="1">
      <stop offset="0" stop-color="var(--slice-light)"/>
      <stop offset="1" stop-color="var(--slice-mid)"/>
    </linearGradient>
  </defs>

  <!-- Brand mark, set vertically along the left edge -->
  <g class="brand">
    <circle class="brand-dot" cx="40" cy="250" r="28"/>
    <text class="brand-name" transform="translate(54 210) rotate(-90)" textLength="195" lengthAdjust="spacingAndGlyphs">CrustVarto</text>
  </g>

  <!-- Half pizza of four slices -->
  <path class="pizza-illustration" role="img" aria-label="Line drawing of half a pizza cut into four slices with scattered black and red toppings"
        d="M645,110 A489,489 0 0 0 645,1088 Z" fill="url(#sliceTone)"/>

  <!-- Slogan -->
  <g class="slogan">
    <text class="slogan-wide ink-black" x="685" y="200" font-size="118" textLength="370" lengthAdjust="spacingAndGlyphs">YOU’LL</text>
    <text class="slogan-tall ink-black" x="685" y="350" font-size="160" textLength="370" lengthAdjust="spacingAndGlyphs">MISS</text>
    <text class="slogan-tall ink-red" x="685" y="500" font-size="148" textLength="370" lengthAdjust="spacingAndGlyphs">100%</text>
    <text class="slogan-wide ink-black" x="685" y="585" font-size="76" textLength="370" lengthAdjust="spacingAndGlyphs">OF THE</text>
    <text class="slogan-tall ink-red" x="685" y="790" font-size="224" textLength="370" lengthAdjust="spacingAndGlyphs">PIZZA</text>
    <text class="slogan-tall ink-black" x="685" y="890" font-size="96" textLength="363" lengthAdjust="spacingAndGlyphs">YOU DON’T</text>
    <text class="slogan-tall ink-red" x="685" y="1085" font-size="218" textLength="360" lengthAdjust="spacingAndGlyphs">EAT</text>
  </g>
</svg>
</body>
</html>
```